Industry automation wholesale website

www.velqora.eu provides solutions for automation, building automation and digital signage.

Our products are rugged, reliable, energy saving and representative.

Scope of pages:
● welcome page
- scope of products
- applications, success stories and news
● category page
- short introduction
- sub categories
- product highlights
● product page
- short introduction
- about 3 to 4 pictures
- technical specifications: materials, dimensions
- price
- related products

Optional:
● contact page
- address
- contact form
● blog
- picture
- text
● logo
● favicon / apple touch icon

Conclusion:
● We need a professionally looking site
● Bright colors (e.g. white, grey, metalic colors, blue)

some pages we like:
http://www.brundafel.de/
http://www.korvimash.de/

Target Market(s)

Our target market is the industrial sector
● Target audience: engineering and IT professionals

Industry/Entity Type

Building

Requirements
Must have
• ● only use free available fonts e.g. Pellor Type Library (http://www.pellortype.com/webfonts)
Should not have
• ● sound
● flash

```html
<!DOCTYPE html>
<html lang="en">
<head>
<meta charset="utf-8">
<title>Velqora – analog digital measurements</title>
<link rel="stylesheet" href="https://fonts.googleapis.com/css2?family=Arimo:ital,wght@0,400;0,700;1,400&display=swap">
<style>
  :root{
    --brand:#1b7bb5;
    --brand-dark:#15608f;
    --nav-active:#e8e8e8;
    --page-bg:#e9e9e9;
    --card:#ffffff;
    --ink:#333333;
    --muted:#6a6a6a;
    --rule:#dddddd;
    --footer:#2e3237;
    --footer-ink:#d8d8d8;
    --hero-top:#d4ecf6;
    --hero-mid:#a9d6ec;
    --hero-low:#8ccbe6;
  }
  *{box-sizing:border-box;margin:0;padding:0}
  html,body{width:1200px;height:639px;overflow:hidden}
  body{position:relative;background:var(--page-bg);font-family:"Arimo",Arial,sans-serif;color:var(--ink)}

  .site-header{position:absolute;left:0;top:0;width:1200px;height:60px;background:#fff}
  .brand{position:absolute;left:355px;top:7px;display:flex;align-items:center;gap:8px;height:34px}
  .brand-name{font-size:36px;font-weight:400;color:var(--brand);letter-spacing:1px;line-height:34px}
  .brand-dot{width:9px;height:9px;border-radius:50%;background:var(--brand)}
  .brand-tagline{position:absolute;left:356px;top:46px;font-size:8.5px;line-height:9px;color:var(--brand);font-weight:700;letter-spacing:.3px}
  .language{position:absolute;left:746px;top:0;width:96px;height:15px;background:#ebebeb;font-size:6.5px;color:#555;display:flex;align-items:center;gap:5px;padding-left:5px}
  .language .select{width:56px;height:10px;background:#fff;border:1px solid #bbb;font-size:6px;padding-left:2px;line-height:8px;position:relative}
  .language .select::after{content:"";position:absolute;right:1px;top:1px;width:7px;height:6px;background:#777}
  .search{position:absolute;left:723px;top:30px;width:121px;height:17px;border:1px solid #ddd;background:#fff;font-size:6.5px;color:#aaa;padding:4px 6px}
  .search-btn{position:absolute;right:-1px;top:-1px;width:16px;height:17px;background:#c8c8c8}

  .main-nav{position:absolute;left:0;top:60px;width:1200px;height:17px;background:var(--brand)}
  .main-nav ul{list-style:none;position:absolute;left:356px;top:0;display:flex;height:17px}
  .main-nav li{font-size:7.5px;color:#fff;padding:0 13px;line-height:17px;letter-spacing:.2px}
  .main-nav li.active{background:var(--nav-active);color:#333}

  .hero{position:absolute;left:0;top:77px;width:1200px;height:205px;background:radial-gradient(ellipse at 55% 40%,#e6f4fa 0%,var(--hero-top) 35%,var(--hero-mid) 75%,var(--hero-low) 100%)}
  .hero-visual{position:absolute;left:369px;top:11px;width:164px;height:176px;border-radius:6px;background:linear-gradient(160deg,#5b5f66 0%,#2c2f34 45%,#4a4e55 100%)}
  .hero-title{position:absolute;left:558px;top:17px;width:300px;font-size:17px;line-height:22px;color:var(--brand);font-weight:400}
  .hero-sub{position:absolute;left:558px;top:66px;font-size:9.5px;font-style:italic;color:#444}
  .hero-list{position:absolute;left:558px;top:89px;list-style:none;font-size:9px;line-height:12px;font-style:italic;color:#444}
  .btn-more{position:absolute;left:763px;top:154px;width:62px;height:22px;background:var(--brand);color:#fff;font-size:8.5px;text-align:center;line-height:22px}

  .content-card{position:absolute;left:348px;top:270px;width:498px;height:316px;background:var(--card);border:1px solid #dcdcdc;border-radius:3px}
  .section-title{font-size:11px;font-weight:400;color:#222}
  .welcome{position:absolute;left:16px;top:13px;width:312px}
  .welcome p{font-size:5.6px;line-height:8.4px;color:#666;margin-top:7px;text-align:justify}
  .products{position:absolute;left:16px;top:122px;width:312px}
  .product-grid{display:flex;gap:11px;margin-top:7px}
  .product{width:96px;position:relative}
  .product-img{height:76px;background:linear-gradient(160deg,#a9d3ef,#5f9fd0);position:relative}
  .product-img.panel{background:linear-gradient(160deg,#c9cdd2,#8d949c)}
  .product-img.box{background:linear-gradient(160deg,#d6d8db,#7e8389)}
  .badge{position:absolute;right:2px;top:2px;width:30px;height:9px;background:#e0232a}
  .product h3{font-size:6.6px;font-weight:700;color:#222;margin-top:6px;line-height:8.5px;height:18px}
  .product p{font-size:5.5px;line-height:8px;color:#666;margin-top:3px;height:32px;overflow:hidden;text-align:justify}
  .read-more{display:inline-block;font-size:5px;line-height:6px;color:#555;border:1px solid #ccc;border-radius:6px;background:#f3f3f3;padding:1px 5px;position:absolute;right:5px;bottom:-12px}

  .sidebar{position:absolute;left:340px;top:13px;width:146px}
  .news-box{margin-top:7px;border:1px solid #e2e2e2;border-radius:3px;height:131px;padding:6px 8px;position:relative}
  .news-item{position:relative;height:37px;border-bottom:1px solid #eee}
  .news-item:nth-child(3){border-bottom:none}
  .news-title{position:absolute;left:0;top:0;display:block;font-size:6.5px;line-height:8px;color:var(--brand);font-weight:700}
  .news-date{position:absolute;right:0;top:0;font-size:5.5px;line-height:8px;color:#aaa}
  .news-thumb{position:absolute;left:0;top:12px;width:17px;height:17px;background:#3d6f95;border-radius:2px}
  .news-text{position:absolute;left:22px;top:12px;width:96px;font-size:5.5px;line-height:8px;color:#777}
  .news-arrow{position:absolute;right:0;top:15px;width:10px;height:10px;border-radius:50%;background:#e4e4e4}
  .news-box .read-more{right:6px;bottom:5px}
  .stories{margin-top:19px}
  .story-box{margin-top:8px;border:1px solid #e2e2e2;border-radius:3px;height:102px;position:relative}
  .story-head{display:flex;align-items:flex-start;gap:6px;background:#f4f8fb;padding:4px 5px 3px 0}
  .quote-icon{width:28px;height:18px;background:var(--brand);flex:none;display:flex;align-items:center;justify-content:center}
  .story-lead{font-size:7.5px;line-height:10px;color:var(--brand)}
  .story-text{font-size:5.5px;line-height:8.3px;color:#777;padding:6px 8px;text-align:justify}
  .story-box .read-more{right:6px;bottom:5px}

  .site-footer{position:absolute;left:0;top:598px;width:1200px;height:41px;background:var(--footer);text-align:center;color:var(--footer-ink)}
  .footer-links{font-size:6px;margin-top:8px}
  .copyright{font-size:6px;margin-top:6px}
</style>
</head>
<body>
  <header class="site-header">
    <div class="brand"><span class="brand-name">velqora</span><span class="brand-dot"></span></div>
    <div class="brand-tagline">analog digital measurements</div>
    <div class="language">Language <span class="select">English</span></div>
    <div class="search">Search<span class="search-btn"></span></div>
  </header>

  <nav class="main-nav">
    <ul>
      <li class="active">HOME</li><li>CATEGORY</li><li>PRODUCTS</li><li>BLOG</li><li>CONTACT</li><li>SHOPPING CART</li>
    </ul>
  </nav>

  <section class="hero">
    <div class="hero-visual" role="img" aria-label="Industrial touch panel computer showing a filter machine control screen"></div>
    <h1 class="hero-title">HMI - Kernix ARC 1.8 GHz, 12.1" TFT, resistive touch screen,</h1>
    <p class="hero-sub">Fanless Human Machine Interface</p>
    <ul class="hero-list">
      <li>- ARC D512 1.8 GHz</li>
      <li>- IP 65 Front</li>
      <li>- optional with Automotive HDD, Fixed Disk CF or Solid State Disks</li>
      <li>- optional Tuxlin / Paneos XP Embedded / Paneos 7 Embedded</li>
      <li>- optional 1024x768 Display resolution</li>
    </ul>
    <div class="btn-more">View More</div>
  </section>

  <main class="content-card">
    <section class="welcome">
      <h2 class="section-title">Welcome to Velqora</h2>
      <p>Lorem Ipsum is simply dummy text of the printing and typesetting industry. Lorem Ipsum has been the industry's standard dummy text ever since the 1500s, when an unknown printer took a galley of type and scrambled it to make a type specimen book. It has survived not only five centuries, but also the leap into electronic typesetting, remaining essentially unchanged.</p>
      <p>It was popularised in the 1960s with the release of Lettrafix sheets containing Lorem Ipsum passages, and more recently with desktop publishing software like Veldus PageCrafter including versions of Lorem Ipsum. It was popularised in the 1960s with the release of Lettrafix sheets containing Lorem Ipsum passages, and more recently with desktop publishing software like Veldus PageCrafter including versions of Lorem Ipsum.</p>
    </section>

    <section class="products">
      <h2 class="section-title">Our Products</h2>
      <div class="product-grid">
        <article class="product">
          <div class="product-img" role="img" aria-label="Blue remote IO modules"><span class="badge"></span></div>
          <h3>Modbus RTU / RS485 Remote IO Modules</h3>
          <p>RS485 Remote IO modules are ideal to realize decentralized distributed IO units over long distances. We provide the whole range.</p>
          <span class="read-more">Read More...</span>
        </article>
        <article class="product">
          <div class="product-img panel" role="img" aria-label="Touch panel industry computer"><span class="badge" style="left:24px;top:30px;right:auto"></span></div>
          <h3>Touch Panel Industry Computer</h3>
          <p>We provide prestigious Touch Panel Computers for your building automation. We also provide Human Machine Interfaces for e.g. plants.</p>
          <span class="read-more">Read More...</span>
        </article>
        <article class="product">
          <div class="product-img box" role="img" aria-label="Embedded automation computer box"><span class="badge"></span></div>
          <h3>Embedded systems for industrial automation</h3>
          <p>We are your specialist partner for industrial automation. We provide individual solutions for unitized measurement and offer more.</p>
          <span class="read-more">Read More...</span>
        </article>
      </div>
    </section>

    <aside class="sidebar">
      <h2 class="section-title">Latest News</h2>
      <div class="news-box">
        <div class="news-item"><span class="news-title">News Title</span><span class="news-date">18.1.2014</span><span class="news-thumb"></span><p class="news-text">Lorem Ipsum is simply dummy text of the printing and typesetting</p><span class="news-arrow"></span></div>
        <div class="news-item"><span class="news-title">News Title</span><span class="news-date">18.1.2014</span><span class="news-thumb"></span><p class="news-text">Lorem Ipsum is simply dummy text of the printing and typesetting</p><span class="news-arrow"></span></div>
        <div class="news-item"><span class="news-title">News Title</span><span class="news-date">18.1.2014</span><span class="news-thumb"></span><p class="news-text">Lorem Ipsum is simply dummy text of the printing and typesetting</p><span class="news-arrow"></span></div>
        <span class="read-more">Read More...</span>
      </div>

      <section class="stories">
        <h2 class="section-title">Success Stories</h2>
        <div class="story-box">
          <div class="story-head">
            <span class="quote-icon"><svg width="12" height="10" viewBox="0 0 12 10"><path d="M1 1h10v6H5l-3 2V7H1z" fill="#fff"/></svg></span>
            <p class="story-lead">Lorem Ipsum is simply dummy text of the printing and typeset-</p>
          </div>
          <p class="story-text">Lorem Ipsum is simply dummy text of the printing and typesetting industry. Lorem Ipsum has been the industry's standard dummy text ever since the 1500s, when an unknown printer took a galley of type and scrambled it to make</p>
          <span class="read-more">Read More...</span>
        </div>
      </section>
    </aside>
  </main>

  <footer class="site-footer">
    <p class="footer-links">Home | Category | Products | Blog | Contact | Shopping cart | Terms and Conditions | Masthead</p>
    <p class="copyright">Copyright © 2014 www.velqora.eu. All Rights Reserved</p>
  </footer>
</body>
</html>
```